Business Card Design

We need a business card design for a new company based in Melbourne Australia. We are financial broker in finance industry. We provide a wide range of finance solutions to our clients including home loans, commercial loans, business facilities, car loans, equipment loans, invoice finance, etc. The company name is from director's personal name. We would like to have a new company logo that includes KT.

Industry/Entity Type

Business

Contact Information for Business Card

company name: KT & Co Finance Pty Ltd
person's name: Kenneth Tollard
role: Managing Director
Mobile: 0417 638 294
fax: 03 9561 2047
Email: kenneth.tollard@ktcofinance.example
Address: Suite 4/718 Marlow Avenue Ferndale East Vic 3187
Credit Licence No.: 382917

```html
<!DOCTYPE html>
<html lang="en">
<head>
<meta charset="utf-8">
<title>KT &amp; Co Finance Pty Ltd – Business Card</title>
<link rel="stylesheet" href="https://fonts.googleapis.com/css2?family=Ultra&family=Arimo:ital,wght@0,400;1,700&family=Cousine&family=Varela+Round&display=swap">
<style>
  :root {
    --card-bg: #ffffff;
    --ink: #111111;
    --brand-blue: #3a5fe8;
    --phone-red: #ee1c1c;
  }
  html, body {
    margin: 0;
    padding: 0;
    overflow: hidden;
    background: var(--card-bg);
  }
  .card {
    position: relative;
    width: 1200px;
    height: 741px;
    background: var(--card-bg);
    overflow: hidden;
    color: var(--ink);
  }
  .brand {
    position: absolute;
    left: 0;
    top: 0;
    width: 1200px;
    height: 260px;
  }
  .brand__name {
    font-family: "Ultra", serif;
    font-size: 112px;
    fill: var(--ink);
  }
  .brand__licence {
    font-family: "Arimo", sans-serif;
    font-size: 18px;
    fill: var(--ink);
  }
  .line {
    position: absolute;
    left: 0;
    width: 1200px;
    margin: 0;
    text-align: center;
    white-space: nowrap;
    line-height: 1.15;
  }
  .person__name {
    top: 255px;
    left: 38px;
    font-family: "Arimo", sans-serif;
    font-style: italic;
    font-weight: 700;
    font-size: 72px;
    color: var(--brand-blue);
    letter-spacing: 1px;
  }
  .person__role {
    top: 333px;
    left: 36px;
    font-family: "Cousine", monospace;
    font-size: 44px;
    letter-spacing: 4px;
  }
  .contact__phone {
    top: 455px;
    left: 30px;
    font-family: "Varela Round", sans-serif;
    font-size: 62px;
    letter-spacing: 6px;
    color: var(--phone-red);
  }
  .contact__email {
    top: 543px;
    left: 30px;
    font-family: "Varela Round", sans-serif;
    font-size: 38px;
  }
  .contact__fax {
    top: 598px;
    left: 30px;
    font-family: "Varela Round", sans-serif;
    font-size: 28px;
  }
  .contact__address {
    top: 650px;
    left: -4px;
    font-family: "Varela Round", sans-serif;
    font-size: 34px;
    letter-spacing: 1px;
  }
</style>
</head>
<body>
  <main class="card">
    <svg class="brand" viewBox="0 0 1200 260" aria-label="KT &amp; Co Finance Pty Ltd, Credit Licence No: 382917">
      <circle class="brand__mark" cx="148" cy="152" r="90" fill="var(--brand-blue)"/>
      <text class="brand__name" x="246" y="190" textLength="900" lengthAdjust="spacingAndGlyphs">KT &amp; Co Finance Pty Ltd</text>
      <text class="brand__licence" x="660" y="212">CREDIT LICENCE NO: 382917</text>
    </svg>

    <p class="line person__name">KENNETH TOLLARD</p>
    <p class="line person__role">Managing Director</p>

    <p class="line contact__phone">0417 638 294</p>
    <p class="line contact__email">kenneth.tollard@ktcofinance.example</p>
    <p class="line contact__fax">Fax 03 9561 2047</p>
    <p class="line contact__address">Suite 4/718 Marlow Ave Ferndale East Vic 3187</p>
  </main>
</body>
</html>
```